Business Card and Stationary for Commercial Real Estate Brokerage
Tarvel Commercial
Business Card and Stationary for Commercial Real Estate Brokerage - Real Estate
Creative Brief
Use specific fonts
Use same as logo font or other, whichever looks best
Professional
Dorian P. Lusk
Senior Vice President
4821 Halbrook Avenue, Newport Beach, CA 92660
dlusk@tarvelpx.example
www.tarvelpx.example
CA DRE: 04263918
Please include additional business location with the following address and contact information in no particular order, as a placeholder: 318 Quillan Avenue, New York, NY 10166 Phone: 347-555-0192 License No. NY DRE: 86420913

```html
<!DOCTYPE html>
<html lang="en">
<head>
<meta charset="utf-8">
<title>Tarvel Commercial – Business Card</title>
<link rel="stylesheet" href="https://fonts.googleapis.com/css2?family=Montserrat:wght@400;500;700&display=swap">
<style>
  :root {
    --backdrop: #e9e9ea;
    --card: #ffffff;
    --navy: #1d3576;
    --blue: #2f5fb5;
    --ink: #4a4d55;
    --icon: #26305a;
  }
  * { box-sizing: border-box; margin: 0; padding: 0; }
  html, body {
    width: 1200px; height: 914px; overflow: hidden;
    background: var(--backdrop);
  }
  body {
    display: flex; align-items: center; justify-content: center;
    font-family: "Montserrat", sans-serif;
  }
  .business-card {
    position: relative;
    width: 980px; height: 560px;
    background: var(--card);
    box-shadow: 0 10px 30px rgba(0,0,0,0.12);
  }
  .brand {
    position: absolute; top: 118px; left: 0; right: 0;
    display: flex; align-items: center; justify-content: center; gap: 18px;
  }
  .brand-mark { width: 30px; height: 30px; background: var(--navy); }
  .brand-name {
    font-weight: 700; font-size: 54px; color: var(--navy);
    letter-spacing: 1px;
  }
  .identity {
    position: absolute; top: 262px; left: 0; right: 0;
    text-align: center;
    font-size: 17px; font-weight: 500; color: var(--blue);
    text-transform: uppercase; letter-spacing: 3px;
  }
  .identity .divider { margin: 0 14px; }
  .contacts {
    position: absolute; top: 330px; left: 90px; right: 60px;
    display: flex; flex-direction: column; gap: 14px;
    font-size: 14px; color: var(--ink);
    text-transform: uppercase; letter-spacing: 1.5px;
  }
  .contact-row { display: flex; align-items: center; gap: 20px; }
  .contact-item { display: flex; align-items: center; gap: 8px; white-space: nowrap; }
  .contact-item svg { width: 16px; height: 16px; flex: none; }
</style>
</head>
<body>
  <main class="business-card">
    <header class="brand">
      <span class="brand-mark"></span>
      <span class="brand-name">Tarvel Commercial</span>
    </header>

    <p class="identity">Dorian P. Lusk<span class="divider">|</span>Senior Vice President</p>

    <section class="contacts">
      <div class="contact-row">
        <span class="contact-item">
          <svg viewBox="0 0 16 16"><circle cx="8" cy="8" r="8" fill="var(--icon)"/><path d="M8 3.5a2.8 2.8 0 0 0-2.8 2.8C5.2 8.4 8 12.5 8 12.5s2.8-4.1 2.8-6.2A2.8 2.8 0 0 0 8 3.5z" fill="#fff"/><circle cx="8" cy="6.3" r="1" fill="var(--icon)"/></svg>
          4821 Halbrook Avenue, Newport Beach, CA 92660
        </span>
        <span class="contact-item">
          <svg viewBox="0 0 16 16"><circle cx="8" cy="8" r="8" fill="var(--icon)"/><path d="M5.3 4.2l1.4-.4.9 2-.9.7a5 5 0 0 0 2.8 2.8l.7-.9 2 .9-.4 1.4c-3.6.4-6.9-2.9-6.5-6.5z" fill="#fff"/></svg>
          949-555-0147
        </span>
      </div>
      <div class="contact-row">
        <span class="contact-item">
          <svg viewBox="0 0 16 16"><circle cx="8" cy="8" r="8" fill="var(--icon)"/><rect x="4" y="5" width="8" height="6" fill="#fff"/><path d="M4 5l4 3.2L12 5" fill="none" stroke="var(--icon)" stroke-width="0.9"/></svg>
          dlusk@tarvelpx.example
        </span>
        <span class="contact-item">
          <svg viewBox="0 0 16 16"><circle cx="8" cy="8" r="8" fill="var(--icon)"/><circle cx="8" cy="8" r="4.2" fill="none" stroke="#fff" stroke-width="1"/><ellipse cx="8" cy="8" rx="1.8" ry="4.2" fill="none" stroke="#fff" stroke-width="0.9"/><path d="M3.8 8h8.4" stroke="#fff" stroke-width="0.9"/></svg>
          www.tarvelpx.example
        </span>
        <span class="contact-item">
          <svg viewBox="0 0 16 16"><circle cx="8" cy="8" r="8" fill="var(--icon)"/><path d="M5.3 4.2l1.4-.4.9 2-.9.7a5 5 0 0 0 2.8 2.8l.7-.9 2 .9-.4 1.4c-3.6.4-6.9-2.9-6.5-6.5z" fill="#fff"/></svg>
          949-555-0110
        </span>
        <span class="contact-item">
          <svg viewBox="0 0 16 16"><circle cx="8" cy="8" r="8" fill="var(--icon)"/><path d="M4.8 8.2l2.1 2.1 4.3-4.5" fill="none" stroke="#fff" stroke-width="1.4"/></svg>
          CA DRE: 04263918
        </span>
      </div>
      <div class="contact-row">
        <span class="contact-item">
          <svg viewBox="0 0 16 16"><circle cx="8" cy="8" r="8" fill="var(--icon)"/><path d="M8 3.5a2.8 2.8 0 0 0-2.8 2.8C5.2 8.4 8 12.5 8 12.5s2.8-4.1 2.8-6.2A2.8 2.8 0 0 0 8 3.5z" fill="#fff"/><circle cx="8" cy="6.3" r="1" fill="var(--icon)"/></svg>
          318 Quillan Avenue, New York, NY 10166
        </span>
        <span class="contact-item">
          <svg viewBox="0 0 16 16"><circle cx="8" cy="8" r="8" fill="var(--icon)"/><path d="M5.3 4.2l1.4-.4.9 2-.9.7a5 5 0 0 0 2.8 2.8l.7-.9 2 .9-.4 1.4c-3.6.4-6.9-2.9-6.5-6.5z" fill="#fff"/></svg>
          347-555-0192
        </span>
        <span class="contact-item">
          <svg viewBox="0 0 16 16"><circle cx="8" cy="8" r="8" fill="var(--icon)"/><path d="M4.8 8.2l2.1 2.1 4.3-4.5" fill="none" stroke="#fff" stroke-width="1.4"/></svg>
          NY DRE: 86420913
        </span>
      </div>
    </section>
  </main>
</body>
</html>
```